buseisness card

design a card that similar to my web site
BRIXENTAPLORLLC .COM

Contact Information for Business Card

NAME PHONE # WEBSITE EMAIL AND DISCTIPTION OF WHAT WE DO

Colors
0054AA
0677BA
7BADD7
CADEEF
E8F1F8

Requirements
Must have
• lOGO AND DETAILS
Nice to have
• I LIKE THE WATER LIKE ON MY WEB SITE

```html
<!DOCTYPE html>
<html lang="en">
<head>
<meta charset="utf-8">
<title>Brixentaplor business card</title>
<link rel="stylesheet" href="https://fonts.googleapis.com/css2?family=Montserrat:wght@400;500;600;700&family=Barlow+Condensed:wght@300;400;600&display=swap">
<style>
  :root {
    --stage: #0b284d;
    --brand-deep: #0054aa;
    --brand-blue: #0677ba;
    --brand-sky: #7badd7;
    --brand-mist: #cadeef;
    --brand-pale: #e8f1f8;
    --ink-navy: #123a66;
    --ink-dark: #222831;
    --eco-green: #5fe07a;
    --white: #ffffff;
  }
  html, body {
    margin: 0;
    padding: 0;
    width: 1200px;
    height: 800px;
    overflow: hidden;
    background: var(--stage);
  }
  .stage {
    position: relative;
    width: 1200px;
    height: 800px;
  }
  .card {
    position: absolute;
    top: 289px;
    width: 429px;
    height: 245px;
    overflow: hidden;
  }
  .card-front {
    left: 146px;
    font-family: "Montserrat", sans-serif;
    text-align: center;
  }
  .water-scene {
    position: absolute;
    inset: 0;
    background:
      radial-gradient(ellipse 60% 30% at 55% 0%, rgba(255,255,255,0.75), rgba(255,255,255,0) 70%),
      linear-gradient(180deg, #3fd0ef 0%, #1aa6da 28%, #1374bf 52%, #1c8fd0 64%, #38c7ea 80%, #7fe3f4 100%);
  }
  .front-content {
    position: absolute;
    inset: 0;
  }
  .brand-name {
    position: absolute;
    top: 68px;
    left: 0;
    right: 0;
    margin: 0;
    font-size: 14px;
    font-weight: 600;
    letter-spacing: 0.2px;
    color: var(--brand-blue);
  }
  .service-title {
    position: absolute;
    top: 101px;
    left: 0;
    right: 0;
    margin: 0;
    font-size: 17.5px;
    font-weight: 700;
    color: var(--white);
  }
  .service-systems {
    position: absolute;
    top: 124px;
    left: 0;
    right: 0;
    margin: 0;
    font-size: 11.5px;
    font-weight: 500;
    color: var(--white);
  }
  .service-systems .accent { color: var(--brand-mist); }
  .eco-line {
    position: absolute;
    top: 150px;
    left: 0;
    right: 0;
    margin: 0;
    font-size: 9.6px;
    line-height: 12.5px;
    font-weight: 500;
    color: var(--ink-navy);
  }
  .eco-line .eco { color: var(--eco-green); }
  .front-url {
    position: absolute;
    top: 191px;
    left: 0;
    right: 0;
    margin: 0;
    font-size: 9.8px;
    color: var(--white);
  }
  .card-back {
    left: 624px;
    background: var(--white);
    font-family: "Barlow Condensed", sans-serif;
  }
  .person-name {
    position: absolute;
    left: 47px;
    top: 40px;
    margin: 0;
    font-size: 23px;
    font-weight: 600;
    color: var(--brand-blue);
  }
  .person-role {
    position: absolute;
    left: 47px;
    top: 68px;
    margin: 0;
    font-size: 16px;
    font-weight: 400;
    color: var(--ink-dark);
  }
  .contact-list {
    position: absolute;
    left: 46px;
    top: 143px;
    margin: 0;
    padding: 0;
    list-style: none;
  }
  .contact-item {
    display: flex;
    align-items: center;
    height: 18.5px;
    font-size: 15.5px;
    font-weight: 300;
    color: var(--ink-dark);
  }
  .contact-icon {
    width: 10px;
    height: 10px;
    margin-right: 8px;
    flex: none;
  }
</style>
</head>
<body>
<main class="stage">
  <section class="card card-front">
    <div class="water-scene" role="img" aria-label="Underwater view of sunlit blue water with light rays and bubbles"></div>
    <div class="front-content">
      <p class="brand-name">BRIXENTAPLOR</p>
      <h1 class="service-title">FOAM PROPORTIONER TESTING</h1>
      <p class="service-systems"><span class="accent">HEF</span>, <span class="accent">AR</span>, AND <span class="accent">AFFF</span> SYSTEM</p>
      <p class="eco-line">AN <span class="eco">ECO</span> FRIENDLY COMPANY DOING<br><span class="eco">ECO</span> FRIENDLY TESTING</p>
      <p class="front-url">www.brixentaplorllc.com</p>
    </div>
  </section>

  <section class="card card-back">
    <h2 class="person-name">Your Name</h2>
    <p class="person-role">Director</p>
    <ul class="contact-list">
      <li class="contact-item">
        <svg class="contact-icon" viewBox="0 0 10 10" aria-hidden="true"><rect x="2.5" y="0.5" width="5" height="9" rx="1" fill="none" stroke="#0677ba" stroke-width="0.9"/><line x1="4.3" y1="8" x2="5.7" y2="8" stroke="#0677ba" stroke-width="0.8"/></svg>
        0044 551 902
      </li>
      <li class="contact-item">
        <svg class="contact-icon" viewBox="0 0 10 10" aria-hidden="true"><path d="M9.5 0.5 L0.5 4.2 L4.2 5.8 L5.8 9.5 Z M9.5 0.5 L4.2 5.8" fill="none" stroke="#0677ba" stroke-width="0.9" stroke-linejoin="round"/></svg>
        name@brixentaplorllc.com
      </li>
      <li class="contact-item">
        <svg class="contact-icon" viewBox="0 0 10 10" aria-hidden="true"><circle cx="5" cy="5" r="4.4" fill="none" stroke="#0677ba" stroke-width="0.9"/><ellipse cx="5" cy="5" rx="1.9" ry="4.4" fill="none" stroke="#0677ba" stroke-width="0.8"/><line x1="0.6" y1="5" x2="9.4" y2="5" stroke="#0677ba" stroke-width="0.8"/></svg>
        brixentaplorllc.com
      </li>
    </ul>
  </section>
</main>
</body>
</html>
```